Forge Kinetic Apex label design for two sports nutrition powders

We need a Label designed done for 2 Products .

1 is a Pre Workout Powder - product name
"Volcor Apex "
2 Is a BCAA Powder product name "Restra Apex "

Please see attached our Brand Logo and I have added some concepts of other brand I would like to use as a base Look .

Black Matt Background is key and the use of Red like examples

Target Market(s)

Sports Nutrition Market

Industry/Entity Type

Nutrition

Font styles to use
Sans Serif

Requirements
Must have
• As per sample packaging I sent we need to make sure its the matt background and label is sharpe
Nice to have
• Very cool label
Should not have
• Open to most things

```html
<!DOCTYPE html>
<html lang="en">
<head>
<meta charset="utf-8">
<title>Volcor Apex – Pre-Workout Label</title>
<link rel="stylesheet" href="https://fonts.googleapis.com/css2?family=Archivo+Black&family=Bebas+Neue&family=Oswald:wght@400;500;600&display=swap">
<style>
  :root {
    --bg: #b9b9b9;
    --label: #262526;
    --label-edge: #1a1a1a;
    --metal-light: #efe6dc;
    --metal-mid: #b9a596;
    --metal-dark: #6f625a;
    --white: #ffffff;
    --red: #e3212b;
    --red-text: #e3262e;
  }
  * { box-sizing: border-box; margin: 0; padding: 0; }
  html, body { width: 1200px; height: 1200px; overflow: hidden; }
  body {
    background: var(--bg);
    display: flex;
    align-items: center;
    justify-content: center;
    font-family: "Oswald", sans-serif;
  }
  .label {
    position: relative;
    width: 1040px;
    height: 820px;
    background: linear-gradient(90deg, var(--label-edge) 0%, var(--label) 10%, var(--label) 90%, var(--label-edge) 100%);
    overflow: hidden;
  }
  .hero-art {
    position: absolute;
    left: 0;
    top: 40px;
    width: 300px;
    height: 450px;
    background: radial-gradient(ellipse at 60% 45%, var(--metal-light) 0%, var(--metal-mid) 40%, var(--metal-dark) 75%, transparent 100%);
    opacity: 0.85;
  }
  .brand {
    position: absolute;
    left: 30px;
    top: 540px;
    display: flex;
    align-items: center;
    gap: 14px;
  }
  .brand-dot {
    width: 34px;
    height: 34px;
    border-radius: 50%;
    background: var(--red);
  }
  .brand-name {
    font-family: "Oswald", sans-serif;
    font-weight: 500;
    font-size: 40px;
    color: var(--white);
    letter-spacing: 1px;
    text-transform: uppercase;
  }
  .nutrition-band {
    position: absolute;
    left: 0;
    top: 640px;
    width: 540px;
    height: 56px;
    background: var(--red);
    display: flex;
    align-items: center;
    padding-left: 30px;
  }
  .nutrition-band span {
    font-family: "Oswald", sans-serif;
    font-weight: 400;
    font-size: 30px;
    color: var(--white);
    letter-spacing: 34px;
  }
  .product {
    position: absolute;
    right: 40px;
    top: 70px;
    text-align: right;
  }
  .product-name {
    font-family: "Archivo Black", sans-serif;
    font-size: 128px;
    line-height: 1;
    background: linear-gradient(180deg, var(--metal-light) 0%, var(--metal-mid) 55%, var(--metal-dark) 100%);
    -webkit-background-clip: text;
    background-clip: text;
    color: transparent;
  }
  .product-sub {
    font-family: "Bebas Neue", sans-serif;
    font-size: 120px;
    line-height: 1;
    margin-top: 14px;
    letter-spacing: 2px;
    background: linear-gradient(180deg, var(--metal-light) 0%, var(--metal-mid) 60%, var(--metal-dark) 100%);
    -webkit-background-clip: text;
    background-clip: text;
    color: transparent;
  }
  .tagline {
    margin-top: 40px;
    font-family: "Oswald", sans-serif;
    font-weight: 600;
    font-size: 30px;
    line-height: 1.3;
    color: var(--white);
  }
  .details {
    position: absolute;
    left: 560px;
    top: 560px;
    font-family: "Oswald", sans-serif;
    font-size: 30px;
    line-height: 1.55;
    color: var(--white);
  }
  .details .type {
    color: var(--red-text);
    text-transform: uppercase;
  }
</style>
</head>
<body>
  <main class="label">
    <div class="hero-art" role="img" aria-label="Metallic illustration of a flexed muscular arm"></div>

    <div class="brand">
      <span class="brand-dot"></span>
      <span class="brand-name">Forge Kinetic Apex</span>
    </div>

    <div class="nutrition-band"><span>NUTRITION</span></div>

    <section class="product">
      <h1 class="product-name">Volcor</h1>
      <div class="product-sub">APEX</div>
      <p class="tagline">Concentrated Pre-Workout Powder<br>for supporting intense focus and<br>energy during exercise</p>
    </section>

    <section class="details">
      <p>Natural &amp; Artificial Flavor</p>
      <p class="type">Powder Dietary Supplement</p>
      <p>Net wt. 3.2oz. (900g.)</p>
    </section>
  </main>
</body>
</html>
```